Tovik Lumen - Magazine

Our client would like a magazine designed for a conceptual novelty based on unconventional views on contemporary issues, including; finance, religion, politics etc.!

The novelty includes 1 main article, supporting images and 12 short poems.
We would like the designer to create page vectors, borders, fonts and other layout design elements.

In the first stage of the competition we request:

Magazine layout - 6 pages( 4 article variations based on article content and 2 poem page designs)

We would like to see high impact, striking vectors and design concepts to compliment the article content. See attached bullet point guide to article to help design page themes.

COMPANY INFO
Writer, poet, researcher and commentator. Our client is interested in sharing art and issues he believes in. Our client would like to design one magazine issue first but has a collection of material to produce a series of magazines in the future. So he is looking to establish a potentially long-term partnership with designer(s).

Target Market(s)

Quick and easy to read, coffee time magazine. Target Market: Male 40yrs+, Intellectual, Open Minded.

Industry/Entity Type

Finance

Font styles to use
Serif
Decorative

Requirements
Must have
• Main Article and Poetry: Space for 1 -2 images per page.
A subtle design feature that connects each page.
Primary colors: Jade Green and some Grayscale.
Secondary Colors: 3rd and 4th color open to designers preference.
Page Dimensions : 7.5in height, 7in width.
Articles: Same color theme, different layout and vector choice, same font color and size.
Poetry: Some design creative freedom. Focus on creating a unique title font incorporating the theme of the poem, Poetry TITLE font must be made a feature design element (poem identity)
Font: See Verdant Explorer magazine styling
Columns: Single or multiple.
All vectors and images should be sourced from craft bazaar.
Nice to have
• Images/pictures that connect with article topic and align with color theme.
Should not have
• Avoid repetition of page design. To do this follow the idea of each paragraph (see attached breakdown)

```html
<!DOCTYPE html>
<html lang="en">
<head>
<meta charset="utf-8">
<title>Tovik Lumen – Poem Pages</title>
<link rel="stylesheet" href="https://fonts.googleapis.com/css2?family=Didact+Gothic&family=Questrial&display=swap">
<style>
  :root {
    --backdrop: #f3f3f2;
    --jade-deep: #1f6b2c;
    --jade: #2f8a3a;
    --jade-light: #6fa84a;
    --camo-olive: #8bb04a;
    --gold-title: #d2d27a;
    --verse-light: #d8ecc8;
    --navy: #2b3465;
    --navy-mid: #5c6790;
    --ice: #f2f6fa;
    --ice-blue: #c9d6e6;
    --verse-dark: #1e2330;
  }
  * { margin: 0; padding: 0; box-sizing: border-box; }
  html, body {
    width: 1200px; height: 1000px; overflow: hidden;
    background: var(--backdrop);
  }
  .spread { position: relative; width: 1200px; height: 1000px; }
  .page {
    position: absolute; top: 242px; width: 527px; height: 490px; overflow: hidden;
  }

  /* Left page – Uniform Order */
  .page--uniform { left: 48px; }
  .uniform-art {
    position: absolute; inset: 0;
    background:
      radial-gradient(ellipse 140px 60px at 80px 30px, var(--camo-olive) 0%, transparent 70%),
      radial-gradient(ellipse 160px 70px at 420px 60px, var(--jade-light) 0%, transparent 70%),
      radial-gradient(ellipse 180px 120px at 130px 260px, #3c8f45 0%, transparent 70%),
      radial-gradient(ellipse 200px 120px at 460px 420px, #3f9450 0%, transparent 70%),
      linear-gradient(160deg, #4f9a3e 0%, var(--jade) 35%, var(--jade-deep) 70%, #2a7a3c 100%);
  }
  .title-band {
    position: absolute; top: 48px; height: 27px; display: flex; align-items: center; padding-left: 16px;
  }
  .page--uniform .title-band {
    left: 0; width: 285px;
    background: linear-gradient(90deg, rgba(225,230,150,.55) 0%, rgba(200,210,120,.35) 70%, rgba(200,210,120,0) 100%);
  }
  .poem-title {
    font-family: "Questrial", sans-serif; font-size: 14px; font-weight: 400; letter-spacing: 1.2px;
  }
  .page--uniform .poem-title { color: var(--gold-title); }
  .poem-author {
    position: absolute; top: 83px; left: 16px;
    font-family: "Questrial", sans-serif; font-size: 10.5px; letter-spacing: .6px;
  }
  .page--uniform .poem-author { color: #e6f0d6; }
  .verse--uniform {
    position: absolute; left: 282px; top: 53px;
    font-family: "Didact Gothic", sans-serif; font-size: 8.6px; line-height: 13.6px;
    color: var(--verse-light);
  }

  /* Right page – Dose Me With The Sly */
  .page--sly {
    left: 620px;
    background:
      radial-gradient(ellipse 330px 280px at 45% 45%, var(--ice) 0%, #e4ebf3 45%, var(--ice-blue) 75%, var(--navy-mid) 100%);
  }
  .vial-art {
    position: absolute; left: 0; bottom: 0; width: 300px; height: 222px;
    background:
      radial-gradient(ellipse 130px 90px at 120px 110px, rgba(70,110,170,.55) 0%, rgba(120,150,200,.25) 55%, transparent 80%),
      radial-gradient(ellipse 120px 50px at 220px 150px, rgba(80,100,160,.45) 0%, transparent 75%);
  }
  .page--sly .title-band {
    left: 0; width: 272px;
    background: linear-gradient(90deg, var(--navy) 0%, rgba(43,52,101,.85) 55%, rgba(43,52,101,0) 100%);
  }
  .page--sly .poem-title { color: #ffffff; }
  .page--sly .poem-author { color: var(--navy); }
  .verse--sly {
    position: absolute; right: 45px; top: 52px; text-align: right;
    font-family: "Didact Gothic", sans-serif; font-size: 8.3px; line-height: 10.4px;
    color: var(--verse-dark);
  }
  .verse--sly p + p { margin-top: 11px; }
</style>
</head>
<body>
<main class="spread">

  <section class="page page--uniform">
    <div class="uniform-art" role="img" aria-label="Green camouflage pattern with surveillance cameras"></div>
    <div class="title-band"><h2 class="poem-title">UNIFORM ORDER</h2></div>
    <p class="poem-author">TOVIK LUMEN</p>
    <div class="verse verse--uniform">
      Uniform Order marches in line<br>
      A scheme with steady hand, since ninety-nine<br>
      A silent shift of rank and file<br>
      It's mostly drab and grey<br>
      In every office too<br>
      Is someone keeping watch?<br>
      'Safety First' the posters read<br>
      Old Colonel, you must see it's by design<br>
      Uniform Order drew the line<br>
      Nothing will return the same<br>
      Only we can take the blame<br>
      The quiet papers signed<br>
      (With fewer and fewer doors to find)<br>
      Control of every stream<br>
      Hospitals and wards alike<br>
      Roads and rails and ports<br>
      Our patience wears away
    </div>
  </section>

  <section class="page page--sly">
    <div class="vial-art" role="img" aria-label="Glass medicine vials and a syringe"></div>
    <div class="title-band"><h2 class="poem-title">DOSE ME WITH THE SLY</h2></div>
    <p class="poem-author">TOVIK LUMEN</p>
    <div class="verse verse--sly">
      <p>Hey, friend,<br>This is the man in grey<br>I've mailed my monthly tally (with seal)<br>And I'm calling to see<br>If there's one more trip to the coast<br>We'll name it a Summit For Healers<br>And let the quiet profit grow</p>
      <p>Isn't it odd<br>How slowly we learn<br>Isn't it odd we don't mind<br>Moving the pieces and never the blame<br>The game we've been playing for ages and ages and ages and...</p>
      <p>Drawn into the merchants of the cure<br>On their methods, silence I'll ensure<br>We don't mean to mend, just extend the trend<br>Count up the margins and the ledgers bend</p>
      <p>Dose me with the sly and let 'em buy<br>Dose me with the sly and let 'em sigh<br>Dose me with a lie and ask not why<br>And if you last another year or two<br>I hope you're wonderfully weak<br>For if you are strong we'll prove you wrong<br>While the people around you agree</p>
      <p>Dose me with the sly and let 'em buy<br>Dose me with the sly and let 'em sigh<br>Dose me with a lie and ask not why<br>Pushing for answers on every side<br>Questions we hate, and so is<br>Sitting down to dine<br>With only labels on your plate</p>
      <p>Healing's a risk but take your tablet on time<br>We'll sell you the fever then sell you the cure<br>If only you knew who writes the textbooks<br>Boardrooms and headlines are part of the hooks<br>Those at the top will decide what you eat<br>Step after step we arrive at defeat</p>
    </div>
  </section>

</main>
</body>
</html>
```